Web Design Project for Energy Efficiency Consultancy

We require a website designed and preferably coded. The website will have around 6-8 pages of basic content with a "contact us" webform.

We are primarily after someone to take our logo, colour scheme and the rough layouts that we have produced and to turn them into a professional looking website.

Please refer to the attached documents for example layouts that we have put together in photoshop, example content, our logo and colour scheme.

We will accept a PSD file but our preference is certainly to have it coded.
Updates

We have attached some documents to the brief that provide more detail.

We have had a question about how projects can be loaded into Venture Lattice. Follow this link for more info http://www.venturelattice.com.au/support/dw#install

Target Market(s)

Builders, real estate agents, government agencies

Industry/Entity Type

It Professional

Requirements
Must have
• We are after a clean and professional look.
Nice to have
• We are keen to have the site fully coded in venture lattice as we have another website that has been built on VL and so we are familiar with how to use it.

```html
<!DOCTYPE html>
<html lang="en">
<head>
<meta charset="utf-8">
<title>Ecovance – Energy Assessment</title>
<link rel="stylesheet" href="https://fonts.googleapis.com/css2?family=PT+Serif&family=Arimo:wght@400;700&display=swap">
<style>
:root{
  --brown:#8d5a14;
  --brown-dark:#7a4c0e;
  --bar:#a67c2e;
  --bottom:#b08438;
  --yellow:#f6c300;
  --head:#8a4a0e;
  --link:#a5681c;
  --foot-link:#f0b54a;
  --text:#4a4a4a;
  --panel:#ffffff;
  --box:#efefef;
  --field:#b88a3a;
}
*{margin:0;padding:0;box-sizing:border-box}
html,body{width:1105px;height:1200px;overflow:hidden;background:#f4f4f4}
body{position:relative;font-family:"Arimo",Arial,sans-serif;color:var(--text)}
.abs{position:absolute}
.hero{left:0;top:0;width:1105px;height:700px;background:linear-gradient(100deg,#e9e2d6 0%,#8f8a7a 22%,#6b6b66 38%,#d8cfbe 55%,#efe6d2 75%,#f3efe6 100%)}
.hero-fade{left:0;top:560px;width:1105px;height:160px;background:linear-gradient(#f4f4f400,#f4f4f4)}
.topbar{left:303px;top:20px;width:802px;height:41px;background:var(--bar)}
.nav{left:303px;top:20px;height:41px;display:flex;font-family:"PT Serif",Georgia,serif;font-size:14px}
.nav a{color:#fff;text-decoration:none;line-height:41px;padding:0 11px}
.nav a.active{background:var(--yellow);padding:0 19px 0 28px;clip-path:polygon(12px 0,100% 0,100% 100%,0 100%)}
.logo{left:172px;top:19px;display:flex;align-items:center;gap:7px;font-family:"PT Serif",Georgia,serif;font-size:19px;color:var(--head)}
.logo i{width:40px;height:40px;border-radius:50%;background:#9dc43a;display:block}
.wing{top:464px;width:30px;height:473px;background:var(--brown)}
.wing.l{left:141px;clip-path:polygon(0 0,100% 0,100% 100%,28px 100%)}
.wing.r{left:932px;clip-path:polygon(0 0,100% 0,2px 100%,0 100%)}
.panel{left:157px;top:452px;width:790px;height:490px;background:var(--panel);border-radius:8px 8px 0 0}
h2{font-family:"PT Serif",Georgia,serif;font-weight:400;color:var(--head);font-size:16px;letter-spacing:.1px}
.ph{background:linear-gradient(#7fb4e6,#e9d85a 55%,#8b8f6a)}
.p{font-size:10px;line-height:14.2px;text-align:justify}
.p b{color:#5a1a0a}
.btn{background:var(--brown);color:#fff;font-size:10.5px;border-radius:3px;text-align:center;line-height:22px}
.dots{left:175px;top:701px;width:473px;border-top:2px dotted #b9a37c}
.services{left:676px;top:471px;width:249px;height:436px;background:var(--box);border-radius:3px}
.services ul{list-style:none;position:absolute;left:17px;top:49px}
.services li{font-size:9.8px;color:var(--link);height:22.1px;padding-left:17px;position:relative}
.services li::before,.flist li::before{content:"";position:absolute;left:0;top:2px;width:5px;height:5px;border:solid currentColor;border-width:1.3px 1.3px 0 0;transform:rotate(45deg)}
.services li::before{color:#555}
.footer{left:0;top:937px;width:1105px;height:217px;background:var(--brown)}
.bottom{left:0;top:1154px;width:1105px;height:46px;background:var(--bottom)}
.footer h2{color:#fff;font-size:14.5px}
.vdiv{top:958px;height:178px;border-left:1px dotted #b88a44}
.flist{list-style:none}
.flist li{font-size:10px;color:var(--foot-link);height:23.7px;padding-left:17px;position:relative}
.flist li::before{color:#fff}
.date{width:46px;height:46px;background:#a57a35;border-radius:3px;color:#fff;text-align:center;font-family:"PT Serif",Georgia,serif;font-size:10.5px;line-height:12px;padding-top:6px}
.date span{display:block;font-size:18px;line-height:18px}
.news{font-size:10px;line-height:12.6px;color:var(--foot-link);width:115px}
.circ{width:25px;height:25px;border-radius:50%;background:#e6ad3c}
.enq{font-size:10px;line-height:17.2px;color:var(--foot-link)}
.enq td{padding:0}
.form label{position:absolute;font-size:10px;color:var(--foot-link);left:763px}
.field{left:817px;width:108px;height:19px;background:var(--field);border-radius:3px}
.copy{left:181px;top:1170px;font-size:10px;color:#4d3410}
.soc{width:24px;height:24px;border-radius:50%;background:#6a3e0a;top:1164px}
</style>
</head>
<body>
<div class="abs hero" role="img" aria-label="Photo of a smiling couple in front of a modern two-storey home with balconies"></div>
<div class="abs hero-fade"></div>

<div class="abs topbar"></div>
<div class="abs logo"><i></i>Ecovance</div>
<nav class="abs nav">
  <a class="active">Home</a><a>About Us</a><a>Commercial service</a><a>Residential Service</a><a>Other Service</a><a>Contact US</a>
</nav>

<div class="abs wing l"></div>
<div class="abs wing r"></div>
<div class="abs panel"></div>

<h2 class="abs" style="left:180px;top:482px">WELCOME TO ECOVANCE</h2>
<div class="abs ph" style="left:180px;top:521px;width:197px;height:164px" role="img" aria-label="Illustration of a yellow multi-storey apartment building"></div>
<p class="abs p" style="left:390px;top:518px;width:257px">Ecovance is an innovator in energy assessment for commercial and residential buildings. We have a wealth of experience in helpping our clients create more energy efficient and environmentally sustainable buildings which is not only mandatory, but will lower your utility bills and increase your resale value. Ecovance is an affiliation between SunForge and ClearPlan Design because both companies wish to provide our clients with a broad range of expertise and a range of services and products.</p>
<div class="abs btn" style="left:591px;top:663px;width:54px">More</div>
<div class="abs dots"></div>

<h2 class="abs" style="left:180px;top:712px">RESIDENTIAL BUILDINGS</h2>
<div class="abs ph" style="left:179px;top:740px;width:94px;height:62px;background:linear-gradient(#3d7fc9,#b8c8d0 50%,#4b7a3a)" role="img" aria-label="Photo of residential apartment blocks"></div>
<p class="abs p" style="left:180px;top:736px;width:221px"><span style="float:left;width:99px;height:68px"></span><b>ACT:</b> BCA Compliance for NEW Single Dwellings or Unit Developments BCA Compliance for Alterations and Extensions ACTHERS Thermal Assessment for Property sale (Mandatory Disclosure) <b>NSW</b> - BCA and BASIX Compliance for new Single Dwellings or Unit DevelopmentsBCA and BASIX Compliance for Alterations and Extensions</p>
<div class="abs btn" style="left:349px;top:886px;width:53px">More</div>

<h2 class="abs" style="left:424px;top:712px">COMMERCIAL BUILDINGS</h2>
<div class="abs ph" style="left:428px;top:740px;width:95px;height:62px;background:linear-gradient(#1e1710,#8a6a44 60%,#2a2018)" role="img" aria-label="Photo of a lit commercial building at night"></div>
<p class="abs p" style="left:428px;top:736px;width:219px"><span style="float:left;width:103px;height:68px"></span><b>ACT</b> :Building Classes 3 to 9 BAC Section J Compliance - Deemed to Satisfy and Verification Method <b>NSW</b> - Building Classes 3 to 9 - BAC Section J Compliance - Deemed to Satisfy and Verification MethodBuilding Class 2 - ACTHERS Thermal Assessment</p>
<div class="abs btn" style="left:593px;top:886px;width:54px">More</div>

<div class="abs services">
  <h2 class="abs" style="left:17px;top:20px">SERVICES</h2>
  <ul>
    <li>Initial design consultation.</li><li>Sketch designs and energy assessment.</li><li>Final consultation and design.</li><li>Building Fabric.</li><li>Full drafting.</li><li>Development approval.</li><li>Construction documentation.</li><li>Entity consultation electrical, water, drainage.</li><li>Building Sealing.</li><li>External Glazing.</li><li>Municipal services approvals.</li><li>Development application and management.</li><li>Air-Conditioning and Ventilation Systems.</li><li>Development application and management.</li><li>Artificial Lighting and Power.</li><li>Hot Water Supply.</li><li>Access for Maintenance.</li>
  </ul>
</div>

<footer>
<div class="abs footer"></div>
<div class="abs bottom"></div>
<div class="abs vdiv" style="left:323px"></div>
<div class="abs vdiv" style="left:534px"></div>
<div class="abs vdiv" style="left:743px"></div>

<h2 class="abs" style="left:180px;top:955px">NAVIGATION</h2>
<ul class="abs flist" style="left:180px;top:993px">
  <li>Home</li><li>About Us</li><li>Commercial service</li><li>Residential Service</li><li>Other Service</li><li>Contact US</li>
</ul>

<h2 class="abs" style="left:348px;top:955px">LATEST NEWS</h2>
<div class="abs date" style="left:348px;top:994px">FEB<span>5</span></div>
<p class="abs news" style="left:401px;top:997px">The Federal Government has recently Energy commercial..</p>
<div class="abs date" style="left:348px;top:1050px">FEB<span>6</span></div>
<p class="abs news" style="left:401px;top:1053px">The Federal Government has recently Energy commercial..</p>
<svg class="abs" style="left:458px;top:1103px" width="57" height="26" viewBox="0 0 57 26">
  <circle cx="13" cy="13" r="12.5" fill="#e6ad3c"/><circle cx="44" cy="13" r="12.5" fill="#e6ad3c"/>
  <path d="M13 8l-5 5 5 5M18 8l-5 5 5 5M39 8l5 5-5 5M44 8l5 5-5 5" fill="none" stroke="#fff" stroke-width="1.6"/>
</svg>

<h2 class="abs" style="left:551px;top:955px">GENERAL ENQUIRIES</h2>
<table class="abs enq" style="left:553px;top:991px;border-collapse:collapse">
  <tr><td colspan="3">PO BOX XX</td></tr>
  <tr><td colspan="3">Fernleigh</td></tr>
  <tr><td colspan="3">ACT 2999</td></tr>
  <tr><td style="width:86px">Phone</td><td style="width:11px">:</td><td>02 6100 0000</td></tr>
  <tr><td>Mark (mobile)</td><td>:</td><td>0400 000 111</td></tr>
  <tr><td>Jenna (mobile)</td><td>:</td><td>0400 000 222</td></tr>
  <tr><td colspan="3">E :mark.dorran@ecovance.example</td></tr>
  <tr><td colspan="3">jenna.whitby@ecovance.example</td></tr>
</table>

<h2 class="abs" style="left:759px;top:955px">QUICK CONTACT</h2>
<div class="form">
  <label style="top:993px">Name :</label><div class="abs field" style="top:989px"></div>
  <label style="top:1017px">Phone :</label><div class="abs field" style="top:1013px"></div>
  <label style="top:1041px">E-mail :</label><div class="abs field" style="top:1037px"></div>
  <label style="top:1064px">Comment :</label><div class="abs field" style="top:1060px;height:44px"></div>
  <div class="abs btn" style="left:871px;top:1110px;width:54px;background:#e6ad3c">Submit</div>
</div>

<p class="abs copy">2012@ ALlright Reswrved.</p>
<div class="abs soc" style="left:838px"></div>
<div class="abs soc" style="left:869px"></div>
<div class="abs soc" style="left:901px"></div>
</footer>
</body>
</html>
```